Fernhollow Services

After a high quality design website. we are a company that provides services to people that own land and need a hand getting on top of the delayed jobs.
would want a number of tab/ pages for the web page.
Home page / About us page / services page / Gallery page. / Contact us page
we offer a wide range of services .listed below

Stock Work (title)

Stock movement
Break feeding
Temporary staffing

Spraying (title)

Spraying weeds
Spraying gorse

Pastures (title)

Fertilizing
Topping

Building (title)

Habitable sheds
Farm sheds
Sheep yards
Cattle yards
Repair farm buildings
Decks
Retaining walls

Fencing (title)

Stock fencing
Post & rail
Stock yards repair
Electric fencing install & repairs

Water Management (title)

Water trough installation
Water scheme install
Water trough cleaning
Farm water maintenance
Water ponds
Ornamental ponds
Drainage

General (title)

Lawn mowing
Hedge trimming
Pruning trees
Metaling drive ways & races
Water blasting
Small digger work
Little tip truck cartage
Home kill management
Mulching gorse
Section clearing

```html
<!DOCTYPE html>
<html lang="en">
<head>
<meta charset="utf-8">
<title>Fernhollow Services</title>
<link rel="stylesheet" href="https://fonts.googleapis.com/css2?family=Montserrat:wght@300;400;600;700;800&family=Roboto:wght@400;500;700&display=swap">
<style>
:root{
  --green:#64a11c;
  --green-dark:#4e8612;
  --green-soft:#7bb530;
  --black:#0b0b0b;
  --text:#2a2a2a;
  --muted:#6f6f6f;
  --light:#f4f4f4;
  --white:#ffffff;
  --star:#f5a400;
}
*{box-sizing:border-box;margin:0;padding:0}
html,body{width:1200px;height:4280px;overflow:hidden}
body{position:relative;background:var(--white);font-family:Roboto,Arial,sans-serif;color:var(--text)}
.abs{position:absolute}
.btn{position:absolute;display:flex;align-items:center;justify-content:center;gap:8px;border-radius:30px;background:var(--green);color:var(--white);font:700 14px Roboto,sans-serif;text-transform:uppercase;letter-spacing:.2px;white-space:nowrap}
.btn .dot{width:13px;height:13px;border-radius:50%;background:var(--white);position:relative}
.btn .dot:after{content:"";position:absolute;left:4px;top:3.5px;border-left:5px solid var(--green);border-top:3px solid transparent;border-bottom:3px solid transparent}
.brand{position:absolute;display:flex;align-items:center;gap:12px;font:700 24px Montserrat,sans-serif;color:var(--green);letter-spacing:.5px;white-space:nowrap}
.brand .mark{width:44px;height:44px;border-radius:50%;border:3px solid var(--green);flex:none}
.brand-stack{line-height:1.1}
.brand-stack span{display:block}
.photo{position:absolute}
.sec-title{position:absolute;left:0;width:1200px;text-align:center;font:300 36px Montserrat,sans-serif;letter-spacing:.5px}
.sec-title b{font-weight:800}
.sec-title span{color:var(--green)}

/* header */
.topline{left:0;top:0;width:1200px;height:4px;background:var(--green)}
.call{left:692px;top:20px;display:flex;gap:12px;align-items:center}
.call .ic{width:36px;height:36px;border-radius:50%;background:var(--green);display:flex;align-items:center;justify-content:center}
.call small{display:block;font-size:11px;color:var(--muted)}
.call strong{font:700 19px Roboto,sans-serif;color:var(--black)}
.nav{right:145px;top:86px;display:flex;gap:36px;font:700 13px Roboto,sans-serif;color:var(--black)}

/* hero */
.hero{left:0;top:115px;width:1200px;height:725px;background:linear-gradient(180deg,#3a5e8a 0%,#8fa9c4 30%,#c9cfc6 45%,#7c9a3e 62%,#4f7a22 80%,#6b5a40 100%)}
.hero-title{position:absolute;left:143px;top:290px;font:800 42px/1.12 Montserrat,sans-serif;color:var(--white);letter-spacing:.3px}
.hero-title span{display:block;font-weight:400}
.hero-text{position:absolute;left:145px;top:400px;width:360px;font:500 16px/1.5 Roboto,sans-serif;color:var(--white)}
.dots{left:567px;top:710px;display:flex;gap:4px}
.dots i{width:10px;height:10px;border-radius:50%;border:1.5px solid var(--white)}
.dots i.on{background:var(--white)}

/* about */
.about-title{left:625px;top:935px;font:800 36px Montserrat,sans-serif;color:var(--black);display:flex;align-items:center;gap:18px}
.about-title span{font-weight:300;color:var(--green)}
.about-title em{display:block;width:64px;height:3px;background:var(--green)}
.about p{position:absolute;left:626px;width:430px;font:400 13.4px/1.75 Roboto,sans-serif;color:var(--muted)}

/* services */
.svc{position:absolute;top:1580px;width:282px;text-align:center}
.svc .ring{width:282px;height:282px;border-radius:50%;background:var(--white);padding:12px}
.svc .ring div{width:100%;height:100%;border-radius:50%}
.svc .badge{width:70px;height:70px;border-radius:50%;background:var(--green);border:4px solid var(--white);margin:-54px auto 0;position:relative;display:flex;align-items:center;justify-content:center}
.svc h3{margin-top:14px;font:700 17px Roboto,sans-serif;color:var(--white);text-transform:uppercase}
.arrow{position:absolute;width:20px;height:20px;border-left:4px solid currentColor;border-bottom:4px solid currentColor}

/* testimonials */
.card{position:absolute;top:3070px;width:381px;height:213px;background:var(--white);border-radius:24px;box-shadow:0 4px 14px rgba(0,0,0,.18);padding:22px 36px 0 95px}
.card .q{font:700 54px/0.8 Georgia,serif;color:var(--green);height:34px}
.card p{margin-top:14px;font:400 13.5px/1.6 Roboto,sans-serif;color:var(--muted)}
.card h4{margin-top:10px;font:700 16px Roboto,sans-serif;color:var(--black)}
.card .stars{color:var(--star);font-size:17px;letter-spacing:1px}
.avatar{position:absolute;top:3122px;width:106px;height:106px;border-radius:50%;background:linear-gradient(135deg,#c9d3da,#5d7387);border:3px solid var(--white);box-shadow:0 2px 8px rgba(0,0,0,.2)}

/* contact */
.ct-head{position:absolute;font:700 20px Roboto,sans-serif;color:var(--white)}
.field{position:absolute;height:39px;background:var(--white);border:1px solid #d8d8d8;font:400 11.5px Roboto,sans-serif;color:#777;padding:12px 14px}
.info{position:absolute;left:698px;display:flex;gap:22px}
.info .ic{width:36px;display:flex;justify-content:center}
.info h5{font:700 14px Roboto,sans-serif;color:var(--white);text-transform:uppercase}
.info p{margin-top:6px;font:400 14px Roboto,sans-serif;color:#e8f3d9}

/* footer */
.fcol{position:absolute;top:3998px;color:var(--white)}
.fcol h6{font:700 15px Roboto,sans-serif;margin-bottom:18px}
.fcol li{list-style:none;font:400 12px Roboto,sans-serif;color:#d8d8d8;margin-bottom:11px}
.fci{display:flex;gap:10px;margin-bottom:12px;font:400 12px/1.35 Roboto,sans-serif;color:#d8d8d8}
.fci b{display:block;color:var(--white);font-size:11px}
.social{left:172px;top:4131px;display:flex;gap:10px}
.social i{width:28px;height:28px;border-radius:50%;border:2px solid var(--white)}
</style>
</head>
<body>

<!-- header -->
<div class="abs topline"></div>
<div class="brand" style="left:150px;top:36px"><span class="mark"></span>FERNHOLLOW SERVICES</div>
<div class="abs call">
  <div class="ic"><svg width="18" height="18" viewBox="0 0 24 24"><path fill="#fff" d="M6.6 10.8c1.4 2.8 3.8 5.1 6.6 6.6l2.2-2.2c.3-.3.7-.4 1-.2 1.1.4 2.3.6 3.6.6.6 0 1 .4 1 1V20c0 .6-.4 1-1 1C10.6 21 3 13.4 3 4c0-.6.4-1 1-1h3.5c.6 0 1 .4 1 1 0 1.3.2 2.5.6 3.6.1.3 0 .7-.2 1z"/></svg></div>
  <div><small>Call Us Today</small><strong>+1 (555) 014 2280</strong></div>
</div>
<div class="btn" style="left:907px;top:20px;width:148px;height:37px;font-size:13px">Get A Quote</div>
<nav class="abs nav"><span>HOME</span><span>ABOUT US</span><span>OUR SERVICES</span><span>OUR GALLERY</span><span>CONTACT US</span></nav>

<!-- hero -->
<div class="abs hero" role="img" aria-label="Farm landscape with red barn, silo, cornfield and dirt road under a cloudy sky"></div>
<svg class="abs" style="left:0;top:680px" width="1200" height="165" viewBox="0 0 1200 165">
  <path d="M0 10 Q600 250 1200 0 L1200 165 L0 165Z" fill="#fff"/>
  <path d="M0 10 Q600 250 1200 0 L1200 14 Q600 270 0 30Z" fill="var(--green)"/>
</svg>
<h1 class="hero-title">FERNHOLLOW<span>SERVICES</span></h1>
<p class="hero-text">Lorem ipsum dolor amet, consectetur adipiscing incididunt ut et dolore magna aliqua.</p>
<div class="btn" style="left:146px;top:475px;width:192px;height:52px">Get Started <span class="dot"></span></div>
<div class="abs dots"><i></i><i></i><i class="on"></i><i></i><i></i></div>

<!-- about -->
<section class="about">
  <div class="photo" style="left:166px;top:918px;width:384px;height:394px;border-radius:50%;background:#111"></div>
  <div class="photo" style="left:176px;top:914px;width:374px;height:384px;border-radius:50%;background:linear-gradient(135deg,#6b8a3a,#2f6fc4 55%,#8a6a3c)" role="img" aria-label="Worker in a blue cap using a drill on a fence post"></div>
  <div class="about-title abs">ABOUT <span>US</span><em></em></div>
  <p style="top:1005px">Lorem ipsum dolor sit amet, consectetur adipiscing elit, do eiusmod tempor incididunt ut labore et dolore magna aliqua. Ut enim ad minim veniam, quis nostrud exercitation ullamco laboris nisi ut aliquip ex ea commodo consequat. Duis aute irure dolor in reprehenderit in voluptate velit esse cillum dolore eu fugiat nulla pariatur.</p>
  <p style="top:1135px">Sed ut perspiciatis unde omnis iste natus sit voluptatem accusantium doloremque laudantium, totam rem aperiam, eaque ipsa quae ab illo architecto beatae vitae sunt explicabo.</p>
  <div class="btn" style="left:626px;top:1240px;width:169px;height:46px">Read More <span class="dot"></span></div>
</section>

<!-- services -->
<svg class="abs" style="left:0;top:1375px" width="1200" height="690" viewBox="0 0 1200 690">
  <defs><linearGradient id="svcbg" x1="0" y1="0" x2="0" y2="1"><stop offset="0" stop-color="#6aa61f"/><stop offset="1" stop-color="#5c9617"/></linearGradient></defs>
  <path d="M0 155 Q600 -95 1200 155 L1200 545 Q600 790 0 545Z" fill="var(--black)"/>
  <path d="M0 168 Q600 -50 1200 168 L1200 530 Q600 745 0 530Z" fill="url(#svcbg)"/>
  <path d="M0 520 Q600 720 1200 520" fill="none" stroke="#fff" stroke-width="4"/>
</svg>
<div class="abs" style="left:0;top:1660px;width:1200px;height:180px;opacity:.18;background:linear-gradient(90deg,#8b2c1a,transparent 30%,transparent 70%,#8b2c1a)" role="img" aria-label="Faded farm buildings behind the services"></div>
<h2 class="sec-title" style="top:1478px;color:#fff">OUR <b>SERVICES</b></h2>
<div class="abs" style="left:570px;top:1530px;width:60px;height:3px;background:#fff"></div>
<div class="svc" style="left:143px">
  <div class="ring"><div role="img" aria-label="Flock of sheep in a pasture" style="background:linear-gradient(180deg,#9db9cf,#c9c2a8 45%,#6f9a3a)"></div></div>
  <div class="badge"><svg width="30" height="30" viewBox="0 0 30 30" fill="none" stroke="#fff" stroke-width="2"><path d="M4 22 Q15 14 26 22"/><path d="M15 20 V8"/><path d="M15 12 Q20 6 24 8 Q20 14 15 14"/></svg></div>
  <h3>Stock Work</h3>
</div>
<div class="svc" style="left:459px">
  <div class="ring"><div role="img" aria-label="Farmer spraying a green crop field" style="background:linear-gradient(180deg,#b7cbdc,#d8d9d0 35%,#3f8a2a)"></div></div>
  <div class="badge"><svg width="30" height="30" viewBox="0 0 30 30" fill="none" stroke="#fff" stroke-width="2"><path d="M6 24 L18 12"/><circle cx="21" cy="9" r="3"/><path d="M12 26 V20 M18 26 V18 M24 26 V20"/></svg></div>
  <h3>Spraying</h3>
</div>
<div class="svc" style="left:773px">
  <div class="ring"><div role="img" aria-label="Gloved hand adding fertilizer to seedlings" style="background:linear-gradient(135deg,#3f7a22,#5a4630 60%,#2b6fb0)"></div></div>
  <div class="badge"><svg width="30" height="30" viewBox="0 0 30 30" fill="none" stroke="#fff" stroke-width="2"><rect x="6" y="14" width="18" height="11" rx="2"/><path d="M15 14 V6 M15 9 Q11 5 9 7 M15 9 Q19 5 21 7"/></svg></div>
  <h3>Pastures</h3>
</div>
<span class="arrow" style="left:66px;top:1710px;color:#fff;transform:rotate(45deg)"></span>
<span class="arrow" style="left:1122px;top:1710px;color:#fff;transform:rotate(-135deg)"></span>

<!-- gallery -->
<h2 class="sec-title" style="top:2122px;color:var(--black)"><b>OUR</b> <span>GALLERY</span></h2>
<div class="photo" style="left:151px;top:2212px;width:444px;height:262px;background:linear-gradient(180deg,#9fb08c,#7d9264)" role="img" aria-label="Pigs in a misty fenced field"></div>
<div class="photo" style="left:605px;top:2212px;width:443px;height:262px;background:linear-gradient(90deg,#3a3a3a,#6a8a4a 55%,#3f6a2a)" role="img" aria-label="Worker water blasting a paved path"></div>
<div class="photo" style="left:151px;top:2483px;width:294px;height:260px;background:linear-gradient(180deg,#a7b8b0,#3e7a2e 45%,#2f5f22)" role="img" aria-label="Tractor spraying rows of crops"></div>
<div class="photo" style="left:454px;top:2483px;width:293px;height:260px;background:linear-gradient(180deg,#7ea84a,#5d9326)" role="img" aria-label="Greenhouse interior with a green overlay"></div>
<div class="abs" style="left:577px;top:2595px;width:40px;height:40px;border-radius:50%;background:#fff;display:flex;align-items:center;justify-content:center"><svg width="18" height="18" viewBox="0 0 20 20" fill="none" stroke="#222" stroke-width="2.2"><circle cx="8" cy="8" r="5.5"/><path d="M12 12 L17 17 M8 5.5 V10.5 M5.5 8 H10.5"/></svg></div>
<div class="photo" style="left:756px;top:2483px;width:292px;height:260px;background:linear-gradient(180deg,#5d7496,#8ea0b0 40%,#4f7f2c)" role="img" aria-label="Red tractor mowing a grassy field"></div>
<div class="btn" style="left:494px;top:2800px;width:212px;height:50px;font-size:13px">View All Gallery <span class="dot"></span></div>

<!-- testimonials -->
<div class="abs" style="left:0;top:2917px;width:1200px;height:520px;background:var(--light)"></div>
<h2 class="sec-title" style="top:2978px;color:var(--black)"><b>WHAT OUR</b> <span>CLIENT SAYS</span></h2>
<div class="card" style="left:196px"><div class="q">&ldquo;</div><p>Sed ut perspiciatis unde omnis iste natus sit voluptatem accusantium doloremque laudantium, totam rem aperiam,</p><h4>Mark Ellison</h4><div class="stars">★★★★★</div></div>
<div class="avatar" style="left:148px" role="img" aria-label="Client portrait"></div>
<div class="card" style="left:672px"><div class="q">&ldquo;</div><p>Sed ut perspiciatis unde omnis iste natus sit voluptatem accusantium doloremque laudantium, totam rem aperiam,</p><h4>Tom Haldane</h4><div class="stars">★★★★★</div></div>
<div class="avatar" style="left:624px" role="img" aria-label="Client portrait"></div>
<span class="arrow" style="left:66px;top:3165px;color:#888;border-width:3px;transform:rotate(45deg)"></span>
<span class="arrow" style="left:1122px;top:3165px;color:#888;border-width:3px;transform:rotate(-135deg)"></span>

<!-- contact + footer background -->
<svg class="abs" style="left:0;top:3350px" width="1200" height="930" viewBox="0 0 1200 930">
  <rect x="0" y="400" width="1200" height="530" fill="var(--black)"/>
  <path d="M0 215 Q600 -115 1200 215 L1200 430 Q600 770 0 430Z" fill="var(--black)"/>
  <path d="M0 230 Q600 -80 1200 230 L1200 415 Q600 735 0 415Z" fill="var(--green)"/>
  <path d="M0 430 Q600 770 1200 430" fill="none" stroke="#fff" stroke-width="3"/>
</svg>
<h2 class="sec-title" style="top:3450px;color:#fff"><b>CONTACT</b> US</h2>
<div class="ct-head" style="left:145px;top:3518px">Get In Touch</div>
<div class="field" style="left:145px;top:3572px;width:238px">&#9711; Name</div>
<div class="field" style="left:398px;top:3572px;width:238px">&#9990; Phone Number</div>
<div class="field" style="left:145px;top:3626px;width:238px">&#9993; Email Address</div>
<div class="field" style="left:398px;top:3626px;width:238px">&#9998; Subject</div>
<div class="field" style="left:145px;top:3678px;width:491px;height:82px">&#9998; Messagge</div>
<div class="btn" style="left:145px;top:3787px;width:107px;height:37px;background:var(--black);font-size:13px">Submit</div>

<div class="ct-head" style="left:698px;top:3518px">Contact Details</div>
<div class="info" style="top:3572px"><div class="ic"><svg width="24" height="32" viewBox="0 0 24 32"><path fill="#fff" d="M12 0C5.4 0 0 5.2 0 11.7 0 20.5 12 32 12 32s12-11.5 12-20.3C24 5.2 18.6 0 12 0zm0 16a4.5 4.5 0 110-9 4.5 4.5 0 010 9z"/></svg></div><div><h5>Address</h5><p>27 Alder Lane, Riverton, NZ 4410</p></div></div>
<div class="info" style="top:3645px"><div class="ic"><svg width="32" height="32" viewBox="0 0 24 24" fill="none" stroke="#fff" stroke-width="1.3"><path d="M6.6 10.8c1.4 2.8 3.8 5.1 6.6 6.6l2.2-2.2c.3-.3.7-.4 1-.2 1.1.4 2.3.6 3.6.6.6 0 1 .4 1 1V20c0 .6-.4 1-1 1C10.6 21 3 13.4 3 4c0-.6.4-1 1-1h3.5c.6 0 1 .4 1 1 0 1.3.2 2.5.6 3.6.1.3 0 .7-.2 1z"/><path d="M14 3a7 7 0 017 7M14 6.5a3.5 3.5 0 013.5 3.5"/></svg></div><div><h5>Phone Number</h5><p>+1 (555) 014 2280</p></div></div>
<div class="info" style="top:3712px"><div class="ic"><svg width="34" height="26" viewBox="0 0 34 26" fill="none" stroke="#fff" stroke-width="2"><rect x="1" y="1" width="32" height="24"/><path d="M1 1 L17 15 L33 1 M1 25 L13 12 M33 25 L21 12"/></svg></div><div><h5>Email</h5><p>info@fernhollowservices.co.nz</p></div></div>

<!-- footer -->
<div class="brand" style="left:150px;top:4030px;font-size:19px;gap:10px"><span class="mark" style="width:40px;height:40px"></span><div class="brand-stack"><span>FERNHOLLOW</span><span>SERVICES</span></div></div>
<div class="abs social"><i></i><i></i><i></i><i></i></div>
<div class="fcol" style="left:423px"><h6>Quick Links</h6><ul><li>Home</li><li>About Us</li><li>Our Services</li><li>Our Gallery</li><li>Contact Us</li></ul></div>
<div class="fcol" style="left:617px"><h6>About Company</h6><ul><li>Legal Information</li><li>Terms &amp; Condition</li><li>Privacy Policy</li><li>Support</li><li>Site Map</li></ul></div>
<div class="fcol" style="left:837px;width:220px"><h6>Contact Us</h6>
  <div class="fci"><span style="color:var(--green)">&#9990;</span><div><b>Phone</b>+1 (555) 014 2280</div></div>
  <div class="fci"><span style="color:var(--green)">&#9993;</span><div><b>Email</b>info@fernhollowservices.co.nz</div></div>
  <div class="fci"><svg width="10" height="14" viewBox="0 0 24 32"><path fill="var(--green)" d="M12 0C5.4 0 0 5.2 0 11.7 0 20.5 12 32 12 32s12-11.5 12-20.3C24 5.2 18.6 0 12 0z"/></svg><div><b>Location</b>27 Alder Lane, Riverton, NZ 4410</div></div>
</div>
<div class="abs" style="left:145px;top:4212px;width:910px;height:1px;background:#333"></div>
<div class="abs" style="left:0;top:4240px;width:1200px;text-align:center;font:400 13px Roboto,sans-serif;color:#d8d8d8">2024 Copyright - Fernhollow Services | All Rights Reserved</div>
<div class="abs" style="left:1120px;top:4188px;width:34px;height:34px;border-radius:50%;background:var(--green);display:flex;align-items:center;justify-content:center"><span style="width:9px;height:9px;border-left:2px solid #fff;border-top:2px solid #fff;transform:rotate(45deg);margin-top:4px"></span></div>

</body>
</html>
```